Website for an electrical contractor :)

We are after a web site which can show pictures of our jobs and our capability in a professional, creative and easily understood way.

----- Brightmoor Electrical ------

We really want a visually good looking website with three sections

Section one:
'Completed projects'
We have a few pictures of jobs which we've completed and would like to show off with a brief description. (see uploads)

Section two:
'Our capabilities'
Just a list of what services we offer

Section three:
We would like a 'contact us' section which people can send us a short msg and upload a file for plans to be able to send to us. We would need their name, phone number and email details. We would also need a short privacy policy saying 'we do not disclose information to third parties'.
We also want to display our contact number and postal address

Good luck :)

Target Market(s)

Adults 25 years+
Business owners
Builders
Real estate agents

Industry/Entity Type

Electrical

Colors

Designer to choose colors to be used in the design.

Requirements
Must have
• Visually appealing
Easy to understand
In the 'Completed projects' section, must have a list for each project we do i can upload pictures for it.

```html
<!DOCTYPE html>
<html lang="en">
<head>
<meta charset="utf-8">
<title>Brightmoor Electrical &amp; Communications</title>
<link rel="stylesheet" href="https://fonts.googleapis.com/css2?family=Oswald:wght@400;500&family=Lato:ital,wght@0,400;0,700;1,400&display=swap">
<style>
:root{
  --red:#e31e25;
  --red-dark:#7d1014;
  --red-nav:#9b1a1e;
  --ink:#2a2a2a;
  --text:#555;
  --grey-bg:#f3f3f3;
  --line:#cfcfcf;
  --quote-bg:#d2d2d2;
  --dark:#555557;
  --white:#fff;
}
*{box-sizing:border-box;margin:0;padding:0}
html,body{width:1200px;height:2848px;overflow:hidden}
body{position:relative;background:var(--white);font-family:"Lato",sans-serif;color:var(--text)}
.abs{position:absolute}

/* header */
.brand{left:125px;top:14px;display:flex;align-items:center;gap:12px}
.brand-dot{width:46px;height:46px;border-radius:50%;background:var(--red)}
.brand-name{font-family:"Lato",sans-serif;font-weight:400;font-size:44px;color:#555;line-height:1}
.brand-sub{left:211px;top:70px;font-size:10px;color:#888;letter-spacing:.5px}
.contact-top{font-size:16px;color:#444;display:flex;align-items:center;gap:8px}
.contact-top svg{width:14px;height:14px;fill:var(--red)}

.nav{left:0;top:110px;width:1200px;height:38px;background:linear-gradient(#a3242a,var(--red-dark));display:flex;justify-content:center}
.nav ul{list-style:none;display:flex;width:950px;justify-content:space-between;align-items:center;padding:0 40px}
.nav li{font-family:"Oswald",sans-serif;font-size:13px;color:var(--white);letter-spacing:.3px}

/* hero */
.hero{left:0;top:148px;width:1200px;height:492px;background:linear-gradient(160deg,#6d5a45 0%,#3a3430 40%,#8c8f8c 70%,#cfd3d0 100%)}
.hero-title{left:0;top:262px;width:1200px;text-align:center;font-family:"Oswald",sans-serif;font-size:40px;color:var(--white);font-weight:400}
.hero-text{left:270px;top:332px;width:660px;text-align:center;font-family:"Oswald",sans-serif;font-size:13px;color:var(--white);line-height:18px}
.btn-red{background:var(--red);color:var(--white);font-family:"Oswald",sans-serif;font-size:13px;display:flex;align-items:center;justify-content:center;gap:8px}
.arrow{width:38px;height:38px;border-radius:50%;display:flex;align-items:center;justify-content:center}
.arrow svg{width:14px;height:14px}

/* section headings */
.heading{left:0;width:1200px;text-align:center;font-family:"Oswald",sans-serif;font-size:34px;color:#333;font-weight:400}
.heading span{color:var(--red)}
.rule{left:125px;width:950px;height:1px;background:#999}

.about-text{left:125px;top:726px;width:950px;font-style:italic;font-size:15px;line-height:21px;color:#444}

/* projects */
.projects{left:0;top:890px;width:1200px;height:775px;background:var(--grey-bg)}
.card{width:300px}
.card-img{width:300px;height:200px;position:relative}
.card-title{font-weight:700;font-size:15.5px;color:#222;margin-top:10px;white-space:nowrap;overflow:hidden}
.card-text{font-size:12.5px;line-height:20px;color:#555;margin-top:2px}
.overlay{position:absolute;left:0;top:14px;width:286px;height:186px;background:rgba(227,30,37,.7);display:flex;justify-content:center;align-items:center;gap:16px}
.overlay i{width:38px;height:38px;border-radius:50%;background:var(--white);display:flex;align-items:center;justify-content:center}
.overlay svg{width:15px;height:15px}
.pager{width:30px;height:30px;background:#333;display:flex;align-items:center;justify-content:center}
.pager svg{width:12px;height:12px}

/* capabilities */
.cap-head{font-family:"Oswald",sans-serif;font-size:25px;color:#333;font-weight:400}
.cap-rule{height:1px;background:#999}
.cap-list{list-style:none;font-size:12.5px;color:#444;line-height:19.6px}
.cap-list li{position:relative;padding-left:22px}
.cap-list li::before{content:"";position:absolute;left:4px;top:7px;width:6px;height:6px;border:1.5px solid var(--red);transform:rotate(45deg)}
.cap-list li.hot{color:var(--red);font-weight:700}

/* testimonial */
.quote-box{left:110px;top:2043px;width:966px;height:124px;background:var(--quote-bg)}
.quote-tail{left:900px;top:2166px;width:0;height:0;border-left:18px solid transparent;border-right:18px solid transparent;border-top:16px solid var(--quote-bg)}
.avatar{left:144px;top:2060px;width:96px;height:96px;border-radius:50%;background:linear-gradient(#6b5a4c,#b9a08a);border:3px solid #eee}
.quote-text{left:278px;top:2063px;width:740px;font-style:italic;font-size:15px;line-height:26px;color:#555}
.quote-mark{font-family:"Oswald",sans-serif;font-size:46px;color:#666;line-height:1}
.dots{left:548px;top:2182px;display:flex;gap:4px}
.dots i{width:9px;height:9px;border-radius:50%;background:#666}

/* contact */
.contact{left:0;top:2230px;width:1200px;height:618px;background:var(--dark)}
.contact-title{left:0;top:2252px;width:1200px;text-align:center;font-family:"Oswald",sans-serif;font-size:32px;color:var(--white);font-weight:400}
.field{left:125px;width:380px;height:36px;border:2px solid #e6e6e6;color:var(--white);font-size:11px;padding:9px 12px}
.upload-icon{right:0;top:0;width:32px;height:32px;background:#777;display:flex;align-items:center;justify-content:center}
.map{left:532px;top:2338px;width:543px;height:382px;background:linear-gradient(135deg,#efece6,#e3e0d8 50%,#d8e6cc)}
.map-band{left:532px;top:2628px;width:543px;height:92px;background:rgba(227,80,85,.85);color:var(--white);font-size:15px;line-height:22px}
.map-band svg{width:15px;height:15px;fill:var(--white);vertical-align:-2px;margin-right:8px}
.footer-rule{left:125px;top:2782px;width:950px;height:1px;background:#777}
.footer-text{left:125px;top:2812px;font-size:11px;color:#bbb}
.socials{left:965px;top:2811px;display:flex;gap:14px}
.socials i{width:10px;height:10px;border-radius:50%;background:#ddd}
</style>
</head>
<body>

<!-- header -->
<div class="abs brand"><span class="brand-dot"></span><span class="brand-name">Brightmoor</span></div>
<div class="abs brand-sub">Electrical &amp; Communications &nbsp;&nbsp;&nbsp;&nbsp;&nbsp;&nbsp;&nbsp;&nbsp;&nbsp;&nbsp;&nbsp;&nbsp; EC5120</div>

<div class="abs contact-top" style="left:812px;top:23px">
  <svg viewBox="0 0 24 24"><path d="M6.6 10.8a15.1 15.1 0 0 0 6.6 6.6l2.2-2.2a1 1 0 0 1 1-.25 11.4 11.4 0 0 0 3.6.6 1 1 0 0 1 1 1V20a1 1 0 0 1-1 1A17 17 0 0 1 3 4a1 1 0 0 1 1-1h3.5a1 1 0 0 1 1 1c0 1.25.2 2.45.6 3.6a1 1 0 0 1-.25 1z"/></svg>0400 555 218
</div>
<div class="abs contact-top" style="left:954px;top:23px">
  <svg viewBox="0 0 24 24"><path d="M7 1h10a2 2 0 0 1 2 2v18a2 2 0 0 1-2 2H7a2 2 0 0 1-2-2V3a2 2 0 0 1 2-2zm0 3v14h10V4z"/></svg>08 9555 3140
</div>
<div class="abs contact-top" style="left:818px;top:61px">
  <svg viewBox="0 0 24 24"><path d="M2 5h20v14H2zm2 2v.5l8 5 8-5V7zm0 2.8V17h16V9.8l-8 5z"/></svg>info@brightmoorelectrical.com.au
</div>

<nav class="abs nav">
  <ul><li>HOME</li><li>ABOUT US</li><li>COMPLETED PROJECTS</li><li>OUR CAPABILITIES</li><li>TESTRIMONIAL</li><li>CONTACT</li></ul>
</nav>

<!-- hero -->
<div class="abs hero" role="img" aria-label="Photo of a finished commercial kitchen fit-out with stainless benches and glass-door fridges"></div>
<h1 class="abs hero-title">Lorem Ipsum is simply dummy text of the printing</h1>
<p class="abs hero-text">There are many variations of passages of Lorem Ipsum available, but the majority have suffered alteration in some form, by injected humour, or randomised words which don't look even slightly believable. If you are going to use a passage of Lorem Ipsum</p>
<div class="abs btn-red" style="left:540px;top:393px;width:110px;height:33px">Know More
  <svg width="12" height="12" viewBox="0 0 24 24"><circle cx="12" cy="12" r="11" fill="#fff"/><path d="M10 7l5 5-5 5" stroke="#e31e25" stroke-width="3" fill="none"/></svg>
</div>
<div class="abs arrow" style="left:24px;top:376px;background:#fff"><svg viewBox="0 0 24 24"><path d="M15 4l-8 8 8 8" stroke="#333" stroke-width="3" fill="none"/></svg></div>
<div class="abs arrow" style="left:1146px;top:376px;background:var(--red)"><svg viewBox="0 0 24 24"><path d="M9 4l8 8-8 8" stroke="#fff" stroke-width="3" fill="none"/></svg></div>

<!-- about -->
<h2 class="abs heading" style="top:662px">ABOUT <span>US</span></h2>
<div class="abs rule" style="top:711px"></div>
<p class="abs about-text">Lorem ipsum dolor sit amet conse ctetur adipisicing elit, sed do eiusmod tempor incididunt ut labore et dolore magna aliqua. Ut enim ad minim veniam, quis nostrud exercitation ullalaboris nisi ut aliquip ex ea commodo consequat.Lorem ipsum dolor sit amet conse ctetur adipisicing elit, sed do eiusmod tempor incididunt ut labore et dolore magna aliqua. Ut eniminimveniam, quis nostrud exercitation ullamco laboris nisi ut aliquip ex ea commodo consequat.Lorem ipsum dolor sit amet conse ctetur adipisicing elit, sed do eiusmod tempor incididunt</p>
<div class="abs btn-red" style="left:531px;top:830px;width:110px;height:35px">Read More</div>

<!-- projects -->
<section class="abs projects"></section>
<div class="abs rule" style="top:889px;background:#ddd"></div>
<h2 class="abs heading" style="top:910px">COMPLETED <span>PROJECTS</span></h2>
<div class="abs rule" style="top:958px"></div>

<div class="abs card" style="left:125px;top:1010px">
  <div class="card-img" role="img" aria-label="Project photo: lounge area with white seating" style="background:linear-gradient(#e9e6e2,#cfc8c2)">
    <div class="overlay">
      <i><svg viewBox="0 0 24 24"><circle cx="10" cy="10" r="6" stroke="#333" stroke-width="3" fill="none"/><path d="M15 15l6 6" stroke="#333" stroke-width="3"/></svg></i>
      <i><svg viewBox="0 0 24 24"><path d="M10 14l4-4M8 12l-3 3a3 3 0 0 0 4 4l3-3M16 12l3-3a3 3 0 0 0-4-4l-3 3" stroke="#333" stroke-width="2.5" fill="none"/></svg></i>
    </div>
  </div>
  <div class="card-title">Lorem Ipsum is simply dummy text of the</div>
  <div class="card-text">There are many variations of passages of Lorem Ipsum available, but the majority have suffered alteration in</div>
</div>
<div class="abs card" style="left:450px;top:1010px">
  <div class="card-img" role="img" aria-label="Project photo: lit community hall interior" style="background:linear-gradient(#3b3833,#8a8378 60%,#b8ad9c)"></div>
  <div class="card-title">Lorem Ipsum is simply dummy text of the</div>
  <div class="card-text">There are many variations of passages of Lorem Ipsum available, but the majority have suffered alteration in</div>
</div>
<div class="abs card" style="left:777px;top:1010px">
  <div class="card-img" role="img" aria-label="Project photo: new townhouse street under blue sky" style="background:linear-gradient(#2d63b8,#6f98d6 50%,#8e8b84 75%,#6f6c66)"></div>
  <div class="card-title">Lorem Ipsum is simply dummy text of the</div>
  <div class="card-text">There are many variations of passages of Lorem Ipsum available, but the majority have suffered alteration in</div>
</div>
<div class="abs card" style="left:125px;top:1306px">
  <div class="card-img" role="img" aria-label="Project photo: concrete industrial unit under construction" style="background:linear-gradient(#4f86cf,#a9c3e4 45%,#d6d3cc 60%,#8d8b86)"></div>
  <div class="card-title">Lorem Ipsum is simply dummy text of the</div>
  <div class="card-text">There are many variations of passages of Lorem Ipsum available, but the majority have suffered alteration in</div>
</div>
<div class="abs card" style="left:450px;top:1306px">
  <div class="card-img" role="img" aria-label="Project photo: building site with brick walls going up" style="background:linear-gradient(#3c72c4,#8fb1e0 40%,#8a6c4c 65%,#a3845f)"></div>
  <div class="card-title">Lorem Ipsum is simply dummy text of the</div>
  <div class="card-text">There are many variations of passages of Lorem Ipsum available, but the majority have suffered alteration in</div>
</div>
<div class="abs card" style="left:777px;top:1306px">
  <div class="card-img" role="img" aria-label="Project photo: empty office floor with ceiling lights" style="background:linear-gradient(#b9b9b7,#5d5c5a 55%,#3a3a39)"></div>
  <div class="card-title">Lorem Ipsum is simply dummy text of the</div>
  <div class="card-text">There are many variations of passages of Lorem Ipsum available, but the majority have suffered alteration in</div>
</div>

<div class="abs pager" style="left:556px;top:1605px"><svg viewBox="0 0 24 24"><path d="M12 6l-6 6 6 6M19 6l-6 6 6 6" stroke="#fff" stroke-width="2.5" fill="none"/></svg></div>
<div class="abs pager" style="left:615px;top:1605px"><svg viewBox="0 0 24 24"><path d="M5 6l6 6-6 6M12 6l6 6-6 6" stroke="#fff" stroke-width="2.5" fill="none"/></svg></div>

<!-- capabilities -->
<h3 class="abs cap-head" style="left:125px;top:1700px">RESIDENTIAL</h3>
<div class="abs cap-rule" style="left:125px;top:1743px;width:460px"></div>
<ul class="abs cap-list" style="left:125px;top:1758px">
  <li class="hot">24hr Support / faults</li><li>RCD (Safety Switch) installations</li><li>Smoke alarms</li><li>Power points</li><li>Lighting points</li><li>External lighting</li><li>Sensor lighting</li><li>Switching</li><li>Antennas and Arial points</li><li>Dimmers</li><li>Ceiling fans</li>
</ul>
<ul class="abs cap-list" style="left:368px;top:1758px">
  <li>Exhaust fans</li><li>Kitchen / Bathroom Projects</li><li>Re-wires</li><li>Smart wiring</li><li>Phone points</li><li>Data points</li><li>Mains/sub mains cabling</li><li>Switchboard installations</li><li>Compliance investigations</li><li>Concrete and wall chasing</li><li>Temporary builders site power</li>
</ul>

<h3 class="abs cap-head" style="left:612px;top:1700px">COMMERCIAL / INDUSTRIAL</h3>
<div class="abs cap-rule" style="left:612px;top:1743px;width:463px"></div>
<ul class="abs cap-list" style="left:612px;top:1758px">
  <li>24hr Support / faults</li><li>Lighting/power design</li><li>Commercial lighting</li><li>Emergency and exit lighting</li><li>Led strip lighting</li><li>Energy efficient lighting</li><li>Temporary lighting</li><li>Illuminated signage</li><li>Switchboard relocations</li><li>Maintenance</li>
</ul>
<ul class="abs cap-list" style="left:857px;top:1758px;width:220px">
  <li>RCD installation</li><li>Phone/data points</li><li>Data cabinets</li><li>Data Networking</li><li>IDF installations/relocations</li><li>All power requirements</li><li>All three phase power requirements</li><li>Electrical rip outs / Disconnections</li><li>Thermal imaging scans</li><li>Concrete and wall chasing</li>
</ul>

<!-- testimonial -->
<div class="abs rule" style="top:1997px;left:0;width:1200px;background:#e6e6e6"></div>
<div class="abs quote-box"></div>
<div class="abs quote-tail"></div>
<div class="abs avatar" role="img" aria-label="Client portrait photo"></div>
<div class="abs quote-mark" style="left:250px;top:2050px">&ldquo;</div>
<p class="abs quote-text">Sed ut perspiciatis unde omnis iste natus error sit voluptatem accusantium doloremque laudantium, totam rem aperiam, eaque ipsa quae ab illo inventore veritatis et quasi architecto beatae vitae dicta sunt explicabo. Nemo enim ipsam voluptatem quia voluptas sit aspernatur aut odit aut fugit <span class="quote-mark" style="font-size:34px;font-style:normal;vertical-align:-10px">&rdquo;</span></p>
<div class="abs dots"><i></i><i></i><i></i><i></i></div>

<!-- contact -->
<section class="abs contact"></section>
<h2 class="abs contact-title">CONTACT US</h2>
<div class="abs" style="left:125px;top:2305px;width:950px;height:1px;background:#888"></div>
<div class="abs" style="left:555px;top:2304px;width:90px;height:3px;background:var(--red)"></div>

<div class="abs field" style="top:2338px">Name :</div>
<div class="abs field" style="top:2388px">Phone :</div>
<div class="abs field" style="top:2437px">Email Address :</div>
<div class="abs field" style="top:2487px">Upload File Your Plans
  <span class="abs upload-icon"><svg width="14" height="14" viewBox="0 0 24 24"><path d="M6 18a5 5 0 0 1-.5-10A7 7 0 0 1 19 9a4.5 4.5 0 0 1-1 9z" fill="#eee"/><path d="M12 16v-6M9 12l3-3 3 3" stroke="#777" stroke-width="2" fill="none"/></svg></span>
</div>
<div class="abs field" style="top:2538px;height:115px">Message :</div>
<div class="abs btn-red" style="left:125px;top:2675px;width:110px;height:45px;font-family:'Lato',sans-serif;font-size:15px">SEND</div>
<div class="abs" style="left:245px;top:2675px;width:110px;height:45px;border:2px solid #eee;color:#fff;display:flex;align-items:center;justify-content:center;font-size:15px">CLEAR</div>

<div class="abs map" role="img" aria-label="Street map showing the office location"></div>
<div class="abs map-band">
  <div class="abs" style="left:30px;top:22px;width:300px">
    <svg viewBox="0 0 24 24"><path d="M12 2a7 7 0 0 0-7 7c0 5 7 13 7 13s7-8 7-13a7 7 0 0 0-7-7zm0 9.5A2.5 2.5 0 1 1 12 6.5a2.5 2.5 0 0 1 0 5z"/></svg>P.O Box 417 Seabrook W.A 6099<br><span style="padding-left:23px">A.B.N: 48 123 456 789</span>
  </div>
  <div class="abs" style="left:352px;top:18px;width:180px;line-height:28px">
    <svg viewBox="0 0 24 24"><path d="M6.6 10.8a15.1 15.1 0 0 0 6.6 6.6l2.2-2.2a1 1 0 0 1 1-.25 11.4 11.4 0 0 0 3.6.6 1 1 0 0 1 1 1V20a1 1 0 0 1-1 1A17 17 0 0 1 3 4a1 1 0 0 1 1-1h3.5a1 1 0 0 1 1 1c0 1.25.2 2.45.6 3.6a1 1 0 0 1-.25 1z"/></svg>0400 555 218<br>
    <svg viewBox="0 0 24 24"><path d="M6.6 10.8a15.1 15.1 0 0 0 6.6 6.6l2.2-2.2a1 1 0 0 1 1-.25 11.4 11.4 0 0 0 3.6.6 1 1 0 0 1 1 1V20a1 1 0 0 1-1 1A17 17 0 0 1 3 4a1 1 0 0 1 1-1h3.5a1 1 0 0 1 1 1c0 1.25.2 2.45.6 3.6a1 1 0 0 1-.25 1z"/></svg>08 9555 3140
  </div>
</div>

<div class="abs footer-rule"></div>
<p class="abs footer-text">© Copy Right 2013-2015 Brightmoor Electrical. &nbsp;&nbsp;|&nbsp;&nbsp; Privacy Policy &nbsp;&nbsp;|&nbsp;&nbsp; All rights reserved.</p>
<div class="abs socials"><i></i><i></i><i></i><i></i><i></i></div>

</body>
</html>
```